Product and Services Brochure for an Oil and Gas Business

Need a brochure design for our Products and Services. I've attached expectations, Product Names, Picture link, Logo. Please ask if you have any questions.

Use Black and/or White background and related bright colors per our logo colors. Design will have black silk laminate and SPOT UV. Hence please define the respective layers and incorporate those feature in the design. Be bold, modern and unique. No cluttered designs.

Pictures link https://files.brindlevault.net/share/7QkT2mWz9pLx4RcVn8JdYe3HsGa6bUo?view=open

Logos - There are two logos that we use. One for square spaces and one for horizontal spaces

Target Market(s)

Industrial

Colors

Designer to choose colors to be used in the design.

Requirements
Must have
• Clean, uncluttered and bold design with good color pairing
Nice to have
• Pictures provided have both black and transparent backgrounds. It will be great (not sure how) but keep the background dynamic so no product pic gets lost or have weird lines
Should not have
• Too much color

```html
<!DOCTYPE html>
<html lang="en">
<head>
<meta charset="utf-8">
<title>TerraGauge Brochure</title>
<link rel="stylesheet" href="https://fonts.googleapis.com/css2?family=Montserrat:wght@500;700;800&family=Open+Sans:wght@400;600;700&display=swap">
<style>
:root{
  --navy:#1d3f7a;
  --navy-deep:#173468;
  --green:#7cb72f;
  --green-light:#9cce4e;
  --paper:#f2f3f3;
  --ink:#24324a;
  --stage:#a9b3c7;
  --grey:#8c949e;
}
*{box-sizing:border-box;margin:0;padding:0}
html,body{width:1200px;height:789px;overflow:hidden}
body{background:var(--stage);font-family:"Open Sans",Arial,sans-serif;position:relative}
.page{position:absolute;top:14px;width:560px;height:760px;background:var(--paper);overflow:hidden;box-shadow:0 6px 18px rgba(30,40,70,.25)}
.cover{left:30px}
.inner{left:610px}
.cover-art{position:absolute;inset:0}
.headline{position:absolute;left:28px;top:104px;width:230px;color:#fff;font-family:"Montserrat",Arial,sans-serif;font-weight:800;font-size:21px;line-height:1.15}
.tagline{position:absolute;right:26px;top:46px;width:250px;color:#fff;font-family:"Montserrat",Arial,sans-serif;font-weight:500;font-size:15px;line-height:1.3;text-align:right}
.product-dot{position:absolute;width:132px;height:132px;border-radius:50%;background:var(--navy-deep);color:#fff;font-family:"Montserrat",Arial,sans-serif;font-weight:700;font-size:13px;display:flex;align-items:center;justify-content:center;text-align:center;line-height:1.25}
.brand{position:absolute;left:30px;bottom:48px;display:flex;align-items:center;gap:10px}
.brand-dot{width:28px;height:28px;border-radius:50%;background:var(--green)}
.brand-name{font-family:"Montserrat",Arial,sans-serif;font-weight:800;font-size:24px;color:var(--green)}
.brand-line{position:absolute;left:68px;bottom:30px;font-size:10px;color:var(--navy);font-weight:600;letter-spacing:.3px}
.contact{position:absolute;right:30px;bottom:24px;width:200px;display:flex;flex-direction:column;gap:6px}
.contact dt{font-family:"Montserrat",Arial,sans-serif;font-weight:700;font-size:11px;color:var(--navy)}
.contact dd{font-size:13px;color:var(--grey)}
.foot-band{position:absolute;left:0;right:0;bottom:0;height:8px;background:var(--green)}

.tab{position:absolute;right:0;background:var(--navy);color:#fff;font-family:"Montserrat",Arial,sans-serif;font-weight:800;font-size:16px;display:flex;align-items:center;padding-left:22px;border-radius:22px 0 0 22px}
.tab-geo{top:28px;width:370px;height:44px}
.tab-cal{top:300px;width:250px;height:40px}
.feature-band{position:absolute;top:82px;right:0;width:380px;height:158px;background:var(--green);border-radius:22px 0 0 22px;padding:14px 20px 0 24px;color:#fff}
.feature-band h3{font-family:"Montserrat",Arial,sans-serif;font-weight:800;font-size:14px}
.feature-band p{font-size:11px;margin:2px 0 4px}
.feature-band ul{font-size:10.5px;padding-left:14px;line-height:1.35}
.photo{position:absolute}
.photo-tubes{top:200px;right:18px;width:320px;height:70px;border-radius:35px;background:linear-gradient(90deg,#e6e6e2 0 18%,#2f5fa8 18% 24%,#1b1d22 24%)}
.photo-cups{top:214px;left:50px;width:110px;height:150px;border-radius:40px 40px 12px 12px;background:linear-gradient(180deg,#8fd63a,#4e9e1c)}
.photo-caliper{top:285px;left:190px;width:90px;height:290px;border-radius:12px;background:linear-gradient(180deg,#d42a33 0 55%,#1b1c22 55%)}
.photo-site{top:520px;right:20px;width:250px;height:212px;border-radius:30px;background:linear-gradient(160deg,#e9ecef,#9ea6ae)}
.copy{position:absolute;left:30px;width:135px;font-size:11px;line-height:1.4;color:var(--ink)}
.copy-a{top:96px}
.copy-b{top:390px;width:150px}
.grey-box{position:absolute;left:30px;top:470px;width:150px;height:90px;border-radius:20px;background:#d9dcdf}
.info-box{position:absolute;left:30px;top:580px;width:150px;height:92px;border-radius:20px;background:var(--navy);color:#fff;font-size:11px;line-height:1.4;padding:14px 16px}
.cal-note{position:absolute;top:352px;right:30px;width:235px;font-size:10.5px;color:var(--ink)}
.cal-head{position:absolute;top:386px;right:30px;width:235px;font-family:"Montserrat",Arial,sans-serif;font-weight:800;font-size:19px;line-height:1.15;color:var(--navy)}
</style>
</head>
<body>
<section class="page cover">
  <svg class="cover-art" width="560" height="760" viewBox="0 0 560 760">
    <defs>
      <linearGradient id="site-tl" x1="0" y1="0" x2="1" y2="1"><stop offset="0" stop-color="#b9c7d6"/><stop offset="1" stop-color="#2b2f36"/></linearGradient>
      <linearGradient id="site-br" x1="0" y1="0" x2="1" y2="1"><stop offset="0" stop-color="#dcdcd8"/><stop offset="1" stop-color="#8a8e92"/></linearGradient>
    </defs>
    <path d="M0 0H560V360Q520 650 260 650H0Z" fill="var(--navy)"/>
    <circle cx="300" cy="390" r="226" fill="none" stroke="var(--green)" stroke-width="12"/>
    <path d="M300 390H80A220 220 0 0 1 300 170Z" fill="url(#site-tl)" role="img" aria-label="Photo: technician loading an inspection tool at a tank site"/>
    <path d="M300 390V170A220 220 0 0 1 520 390Z" fill="var(--green)"/>
    <path d="M300 390H520A220 220 0 0 1 300 610Z" fill="url(#site-br)" role="img" aria-label="Photo: inspection tool resting on gravel near pipework"/>
    <path d="M300 390V610A220 220 0 0 1 80 390Z" fill="var(--navy)"/>
    <line x1="70" y1="390" x2="530" y2="390" stroke="#fff" stroke-width="10"/>
    <line x1="300" y1="160" x2="300" y2="620" stroke="#fff" stroke-width="10"/>
    <g font-family="Montserrat, Arial, sans-serif" font-weight="700" font-size="11" fill="var(--navy)" text-anchor="middle">
      <circle cx="352" cy="222" r="30" fill="#fff"/><text x="352" y="226">PX-Flex</text>
      <circle cx="418" cy="244" r="30" fill="#fff"/><text x="418" y="248">PX-Omni</text>
      <circle cx="466" cy="310" r="30" fill="#fff"/><text x="466" y="314">PX-Geo</text>
    </g>
    <circle cx="300" cy="390" r="62" fill="#fff"/>
    <circle cx="300" cy="390" r="48" fill="var(--navy)"/>
    <circle cx="300" cy="390" r="32" fill="var(--green)"/>
  </svg>
  <h1 class="headline">In-Line Inspection<br>Made Easy</h1>
  <p class="tagline">Simpler solutions to complex Pipeline Inspection Problems</p>
  <div class="product-dot" style="left:40px;top:500px">Geophone +<br>PX-Transmitter</div>
  <div class="product-dot" style="left:190px;top:520px">PX-Caliper</div>
  <div class="brand"><span class="brand-dot"></span><span class="brand-name">TerraGauge</span></div>
  <p class="brand-line">Pipeline Inspection Solutions</p>
  <dl class="contact">
    <div><dt>Your Phone:</dt><dd>+00 000 000 0000</dd></div>
    <div><dt>Email:</dt><dd>hello@terragauge-example.com</dd></div>
  </dl>
  <div class="foot-band"></div>
</section>

<section class="page inner">
  <h2 class="tab tab-geo">GEOPHONE + PX-TRANSMITTER</h2>
  <div class="feature-band">
    <h3>Simple yet Highly Functional Geophone</h3>
    <p>World's first Disposable Transmitter</p>
    <ul>
      <li>Highest and Constant signal strength through entire life.</li>
      <li>Buy it for the price you rent.</li>
      <li>Lower Financial liability.</li>
    </ul>
  </div>
  <div class="photo photo-tubes" role="img" aria-label="Photo: disposable transmitter tubes"></div>
  <p class="copy copy-a">Our molded cups are made in-house with a premium urethane that stays tougher and lasts longer in every pipeline run.</p>
  <div class="photo photo-cups" role="img" aria-label="Photo: green urethane sealing cups"></div>
  <div class="photo photo-caliper" role="img" aria-label="Photo: caliper tool with red sensor rings"></div>
  <h2 class="tab tab-cal">PX-CALIPER</h2>
  <p class="cal-note">PX-Caliper and PX-Def are combined into PX-Caliper</p>
  <p class="cal-head">A versatile platform for all Geometry and Mapping Inspection requirements</p>
  <p class="copy copy-b">Choose the tool you want it to be, with sealing cups, cleaning brushes, magnets and a tracker.</p>
  <div class="grey-box"></div>
  <div class="info-box">Add the mapper option for full location information during tracking.</div>
  <div class="photo photo-site" role="img" aria-label="Photo: snowy pipeline site with inspection tool"></div>
</section>
</body>
</html>
```